We are a small NZ based company looking to rebrand our eco chem free cleaning product Brisko

This product was launched in 2021. The brand and labeling were aimed at the consumer who cared that the cleaning products they bought into their home were not only effective but non-harmful to their families and the environment. The label was a little bohemian/ natural. We feel that the labels now need to be more chic and classy, They need to look stylish in a country cottage as well as a high end minimalist home. Colours need to be mute so as to fit with most decors.
We need help with font colour and type - layout and balance. Trigger/ pump colour.
I have attached photos of our current range and labels
A couple of mock ups we are working on - (struggling with )
A colour pallet
The two last PNG files are closer to where we want to end up but they are not really right.

The products are sold online only
Our website is www.brisko.co.nz
The Brand board that we had done sometime ago is that last file.
Most of the colours on the labels are ok - except the apricot on the foaming hand soap bottle and the colour on the all purpose bottle - neither of which we love.
The Fair Harbour bottles are closer to what we are thinking.
Canva Links
https://www.draftpad.example/design/QWRTyu12abc/pLmNoPqRsTuVwXyZ12AbCd/edit
https://www.draftpad.example/design/QWRTzk34def/hGfEdCbAzYxWvUtSr34EfG/edit
https://www.draftpad.example/design/QWRTmn56ghi/tRsQpOnMlKjIhGfE56HiJk/edit
https://www.draftpad.example/design/QWRTbv78jkl/mNbVcXzLkJhGfDsA78LmNo/edit

Target Market(s)

Mothers who care about the products they bring into there homes but also want the product to look good in the home

Industry/Entity Type

Cleaning products

Requirements
Must have
• Design must be chic - and be able to sit and look great in any modern bathroom or kitchen.

```html
<!DOCTYPE html>
<html lang="en">
<head>
<meta charset="utf-8">
<title>Brisko — Label Range</title>
<link rel="stylesheet" href="https://fonts.googleapis.com/css2?family=Lato:wght@400;700&family=Montserrat:wght@500;600&display=swap">
<style>
  :root {
    --paper: #ffffff;
    --ink: #111111;
    --rule: #6a6a6a;
    --accent-laundry: #5f8f96;
    --accent-concentrate: #f3b928;
    --accent-oxy: #a3a8ad;
    --accent-bathroom: #82b597;
    --accent-glass: #a9dde6;
    --accent-allpurpose: #d3a9a9;
  }
  * { box-sizing: border-box; margin: 0; padding: 0; }
  html, body { width: 1200px; height: 1200px; overflow: hidden; background: var(--paper); }
  body { position: relative; color: var(--ink); font-family: "Lato", sans-serif; }

  .label { position: absolute; }
  .label__body { position: absolute; top: 0; left: 0; }
  .label--centered .label__body { text-align: center; }
  .accent-bar { position: absolute; top: 0; right: 0; width: 6px; height: 100%; }

  .brand { display: inline-flex; align-items: center; gap: 3px; }
  .brand__dot { width: 8px; height: 8px; border-radius: 50%; background: var(--ink); }
  .brand__name { font-family: "Lato", sans-serif; font-weight: 400; font-size: 13px; line-height: 1; }
  .tagline {
    font-family: "Montserrat", sans-serif; font-weight: 600; font-size: 3.4px;
    padding-top: 2px; margin-top: 2px; border-top: 0.6px solid var(--ink); display: inline-block;
  }

  .title { font-weight: 700; font-size: 22px; line-height: 23px; letter-spacing: -0.2px; }
  .label--spray .title { font-size: 21px; line-height: 21px; }

  .strap {
    font-family: "Montserrat", sans-serif; font-weight: 500; font-size: 6.3px;
    letter-spacing: 2.2px; line-height: 8px; text-transform: uppercase;
  }
  .strap--ruled { border-top: 0.6px solid var(--rule); padding-top: 4px; display: inline-block; }

  .uses { list-style: none; display: flex; align-items: center; font-family: "Montserrat", sans-serif; font-size: 4.6px; font-weight: 500; }
  .uses li { padding: 0 5px; border-left: 0.6px solid var(--ink); line-height: 10px; }
  .uses li:first-child { border-left: none; padding-left: 0; }
  .label--centered .uses { justify-content: center; }

  .volume { font-family: "Montserrat", sans-serif; font-size: 5.6px; font-weight: 500; }
  .spark { display: inline-block; vertical-align: middle; }

  .subhead { display: flex; align-items: center; justify-content: center; gap: 8px; }
  .subhead__text {
    font-family: "Montserrat", sans-serif; font-weight: 500; font-size: 6.3px; letter-spacing: 2px;
    line-height: 8px; border-top: 0.6px solid var(--rule); border-bottom: 0.6px solid var(--rule); padding: 5px 6px;
  }
  .note { font-family: "Montserrat", sans-serif; font-size: 4.4px; font-weight: 500; }
</style>
</head>
<body>

<svg width="0" height="0" style="position:absolute">
  <symbol id="sparkle" viewBox="0 0 20 20">
    <path d="M10 0 C11 7 13 9 20 10 C13 11 11 13 10 20 C9 13 7 11 0 10 C7 9 9 7 10 0Z" fill="#111"/>
  </symbol>
</svg>

<!-- Laundry Liquid -->
<article class="label label--centered" style="left:258px; top:260px; width:158px; height:160px;">
  <div class="label__body" style="width:150px; padding-top:11px;">
    <div class="brand"><span class="brand__dot"></span><span class="brand__name">Brisko</span></div><br>
    <p class="tagline">Protect Your Family with Brisko</p>
    <h2 class="title" style="margin-top:11px;">Laundary<br>
      <svg class="spark" width="13" height="13"><use href="#sparkle"/></svg>Liquid
      <svg class="spark" width="7" height="7"><use href="#sparkle"/></svg></h2>
    <p class="strap strap--ruled" style="margin-top:4px;">The Power of<br>Chamomile</p>
    <ul class="uses" style="margin-top:8px;"><li>Machine</li><li>Handwash</li><li>Soaker</li><li>Stain Remover</li></ul>
    <p class="volume" style="margin-top:4px;">500ml</p>
  </div>
  <span class="accent-bar" style="background:var(--accent-laundry);"></span>
</article>

<!-- Concentrate -->
<article class="label label--centered" style="left:545px; top:260px; width:161px; height:160px;">
  <div class="label__body" style="width:150px; padding-top:11px;">
    <div class="brand"><span class="brand__dot"></span><span class="brand__name">Brisko</span></div><br>
    <p class="tagline">Protect Your Family with Brisko</p>
    <h2 class="title" style="margin-top:11px;">Concentrate</h2>
    <div class="subhead" style="margin-top:9px;">
      <svg class="spark" width="7" height="7"><use href="#sparkle"/></svg>
      <span class="subhead__text">MUTI-PURPOSE<br>CLEANER</span>
      <svg class="spark" width="7" height="7"><use href="#sparkle"/></svg>
    </div>
    <p class="note" style="margin-top:8px;">Gentle On You Gentle On Your Planet</p>
    <p class="volume" style="margin-top:14px;">500ml</p>
  </div>
  <span class="accent-bar" style="background:var(--accent-concentrate);"></span>
</article>

<!-- Oxy Soak -->
<article class="label label--centered" style="left:836px; top:260px; width:161px; height:160px;">
  <div class="label__body" style="width:150px; padding-top:11px;">
    <div class="brand"><span class="brand__dot"></span><span class="brand__name">Brisko</span></div><br>
    <p class="tagline">Protect Your Family with Brisko</p>
    <h2 class="title" style="margin-top:11px;">
      <svg class="spark" width="13" height="13" style="margin-right:8px;"><use href="#sparkle"/></svg>OXY<br>SOAK
      <svg class="spark" width="7" height="7"><use href="#sparkle"/></svg></h2>
    <p class="strap strap--ruled" style="margin-top:4px;">Fragrance<br>Free</p>
    <ul class="uses" style="margin-top:6px;"><li>Remove Stains<br>&amp; Odours</li><li>Sanitises</li><li>Whitens &amp; Brightens<br>Laundry</li></ul>
    <p class="volume" style="margin-top:3px;">500ml</p>
  </div>
  <span class="accent-bar" style="background:var(--accent-oxy);"></span>
</article>

<!-- Bathroom Cleaner -->
<article class="label label--spray" style="left:176px; top:845px; width:131px; height:150px;">
  <div class="label__body" style="padding-top:11px;">
    <div class="brand"><span class="brand__dot"></span><span class="brand__name">Brisko</span></div><br>
    <p class="tagline">Protect Your Family with Brisko</p>
    <h2 class="title" style="margin-top:10px;">Bathroom<br>Cleaner</h2>
    <p class="strap strap--ruled" style="margin-top:5px; width:70px;">The Power of<br>Chamomile</p>
    <ul class="uses" style="margin-top:5px;"><li>Shower</li><li>Bath</li><li>Toilet</li><li style="border:none; padding-left:14px;">500ml</li></ul>
  </div>
  <span class="accent-bar" style="background:var(--accent-bathroom);"></span>
</article>

<!-- Glass Cleaner -->
<article class="label label--spray" style="left:447px; top:845px; width:112px; height:150px;">
  <div class="label__body" style="padding-top:10px;">
    <div class="brand"><span class="brand__dot"></span><span class="brand__name">Brisko</span></div><br>
    <p class="tagline">Protect Your Family with Brisko</p>
    <h2 class="title" style="margin-top:9px;">Glass
      <svg class="spark" width="6" height="6" style="vertical-align:top;"><use href="#sparkle"/></svg><svg class="spark" width="11" height="11"><use href="#sparkle"/></svg><br>Cleaner</h2>
    <p class="strap strap--ruled" style="margin-top:5px;">The Power of<br>Chamomile</p>
    <ul class="uses" style="margin-top:4px; font-size:3.4px;"><li>Windows</li><li>Glass</li><li>Stainless Steel</li><li>Reflective Glass</li></ul>
  </div>
  <span class="accent-bar" style="background:var(--accent-glass);"></span>
</article>

<!-- All Purpose Cleaner -->
<article class="label label--spray" style="left:685px; top:845px; width:131px; height:150px;">
  <div class="label__body" style="padding-top:10px;">
    <div class="brand"><span class="brand__dot"></span><span class="brand__name">Brisko</span></div><br>
    <p class="tagline">Protect Your Family with Brisko</p>
    <h2 class="title" style="margin-top:10px;">All Purpose<br>Cleaner</h2>
    <p class="strap strap--ruled" style="margin-top:5px; width:70px;">The Power of<br>Chamomile</p>
    <ul class="uses" style="margin-top:5px;"><li>Surfaces</li><li>Stains</li><li>Grease &amp; Grime</li></ul>
    <p class="volume" style="margin-top:4px;">500ml</p>
  </div>
  <span class="accent-bar" style="background:var(--accent-allpurpose);"></span>
</article>

<!-- Foaming Cleaner -->
<article class="label label--spray" style="left:961px; top:872px; width:100px; height:120px;">
  <div class="label__body" style="padding-top:0;">
    <div class="brand"><span class="brand__dot"></span><span class="brand__name">Brisko</span></div><br>
    <p class="tagline">Protect Your Family with Brisko</p>
    <h2 class="title" style="margin-top:10px;">Foaming<br>Cleaner</h2>
    <p class="strap strap--ruled" style="margin-top:5px; width:68px;">The Power of<br>Chamomile</p>
    <ul class="uses" style="margin-top:5px;"><li>Hands</li><li>Body</li><li>Face</li><li style="border:none; padding-left:12px;">500ml</li></ul>
  </div>
</article>

</body>
</html>
```